Tri-Fold Brochure for Christian Author and Speaker

Lorena Watkiss is an inspirational author and speaker, sharing her testimony and encouraging others in their walk with Christ. A gifted writer, her work has been featured on Gently Radiant, Morning Vessels, and Hymn & Tea Journal (Fall 2011).

Lorena ‘s first book, Leaving the Lantern Hall: Revealing Hidden Snares in Ordinary Routines, is an informative memoir and Bible study, recounting her journey from committed Christian to witch, medium, and ghost hunter for eight years until restored to faith in Jesus Christ. She was a contributing author to Walking the Shadow Road: A Plain Account of Dark Arts from Past Seekers by Dale Winterbottom and a consultant for the novel The Keeper of Pellam Hollow by Lumen Prize Winning Author, Norma Quillfeather.

Lorena’s second book, An Insider’s Guide to Spiritual Warfare: 20 Battle-Tested Strategies from Behind Enemy Lines, will be published by Ridgeway Press for Fall 2014.

Lorena is a wife and mother. She enjoys writing, spending time with her family, taking long walks, listening to music of all kinds, and experiencing God’s daily gift called life.

You can read more about Lorena and see the look and feel we are going for at www.lorenawatkiss.example

The brochure is to be used as a promotional tool to gain Lorena speaking engagements. You can see the topics she covers at http://www.lorenawatkiss.example/speaking-engagements/.

More info can be found at: https://www.social.example/AuthorLorenaWatkiss
https://www.social.example/VMUCX
https://www.social.example/LeavingtheLanternHall
https://www.social.example/TallOakOutreach
http://www.talloakoutreach.example

I have uploaded 3 headshots, book covers for both of Lorena's books and the design layout in .EPS format from Quickprintly.example where I will be getting printing done.

3 more days till the contest ends get your final designs in.

Reason: I'm extending this as I am tied up at a leadership conference and will not be able to give this the attention it deserves till the weekend.

Target Market(s)

Churches and women's groups. Lorena's current audience skews heavy to women on a 70/30 ratio.

Industry/Entity Type

Christian

Requirements
Must have
• Headshot I have uploaded 3
Quotes from previous speaking engagements you can find those at http://www.lorenawatkiss.example/speaking-engagements/

```html
<!DOCTYPE html>
<html lang="en">
<head>
<meta charset="utf-8">
<title>Lorena Watkiss – Speaker Brochure</title>
<link href="https://fonts.googleapis.com/css2?family=Source+Sans+3:ital,wght@0,400;0,600;0,700;1,600;1,700&family=Crimson+Text:ital,wght@1,400;1,600&display=swap" rel="stylesheet">
<style>
:root{
  --purple:#5b2a86;
  --violet:#7d4fa0;
  --teal:#5fc4b0;
  --navy:#2b2a7a;
  --orange:#f9bf7e;
  --blue:#1f6db4;
  --deep-blue:#1d56a8;
  --peach-light:#fdebd9;
  --peach:#f8c697;
  --white:#ffffff;
  --sans:"Source Sans 3", Arial, sans-serif;
  --serif:"Crimson Text", Georgia, serif;
}
*{box-sizing:border-box;margin:0;padding:0}
html,body{width:1200px;height:1000px;overflow:hidden;background:var(--white)}
body{position:relative;font-family:var(--sans);color:var(--navy)}
.panel{position:absolute;overflow:hidden;box-shadow:0 4px 12px rgba(0,0,0,.25)}

/* ---------- Outside panel ---------- */
.outside{left:14px;top:16px;width:620px;height:480px;background:var(--white)}
.bio{position:absolute;left:18px;top:14px;width:360px;font-size:9.5px;font-weight:600;line-height:1.3}
.bio p{margin-bottom:9px}
.bio .booking{text-align:center;margin-top:4px}
.site-link{position:absolute;left:110px;top:120px;font-size:16px;font-weight:700;color:var(--purple)}
.first-book{position:absolute;left:394px;top:10px;width:186px;font-size:9.5px;font-weight:600;line-height:1.25}
.first-book strong{color:var(--violet);font-size:11px}
.vertical-word{position:absolute;z-index:2;writing-mode:vertical-rl;font-weight:700;color:var(--teal);letter-spacing:1px;line-height:1}
.authorship{right:6px;top:8px;font-size:23px}
.topics-band{position:absolute;left:0;top:150px;width:620px;height:160px;background:var(--orange)}
.topics-word{left:16px;top:185px;font-size:30px;transform:rotate(180deg)}
.topics-heading{position:absolute;left:120px;top:162px;font-size:12px;font-weight:700;color:var(--violet)}
.topics-list{position:absolute;left:62px;top:186px;list-style:disc;color:var(--violet);font-size:12.5px;font-weight:700;font-style:italic;line-height:1.35}
.topics-list small{font-size:6px;font-weight:600}
.photo{border-radius:50%;border:3px solid var(--purple);overflow:hidden}
.outside .photo{position:absolute;left:325px;top:122px;width:146px;height:146px;z-index:1}
.credits{position:absolute;z-index:1;left:470px;top:134px;width:112px;text-align:right;font-size:9.5px;font-weight:600;line-height:1.25}
.credits strong{color:var(--violet);font-size:11px}
.books-band{position:absolute;left:0;top:310px;width:620px;height:170px;background:var(--blue)}
.ribbon{position:absolute;left:14px;top:312px;width:402px;height:18px;background:var(--purple);color:var(--white);font-size:8.5px;font-weight:700;font-style:italic;line-height:18px;text-align:center;transform:rotate(-1deg)}
.cover{position:absolute}
.cover-one{left:22px;top:348px;width:70px;height:102px}
.cover-two{left:106px;top:342px;width:72px;height:110px}
.books-copy{position:absolute;left:196px;top:346px;width:410px;color:var(--white);font-size:8.5px;font-style:italic;font-weight:600;line-height:1.3}
.books-copy p{margin-bottom:8px}
.store{position:absolute;left:300px;top:420px;width:240px;text-align:center;color:var(--white);font-size:11.5px;font-style:italic;font-weight:600;line-height:1.6}

/* ---------- Inside panel ---------- */
.inside{left:566px;top:505px;width:626px;height:425px;background:linear-gradient(120deg,var(--peach-light),var(--peach))}
.speaker-heading{position:absolute;left:100px;top:10px;font-size:11px;font-weight:700;color:var(--violet)}
.quotes{position:absolute;left:20px;top:30px;width:370px;font-family:var(--serif);font-style:italic;font-size:8.6px;line-height:1.2;color:#3a2a2a}
.quote{margin-bottom:8px}
.quote cite{display:block;text-align:right;font-family:var(--sans);font-size:5.5px;font-style:normal;margin-top:2px}
.wrap-gap{float:right;width:0;height:46px}
.wrap-box{float:right;clear:right;width:168px;height:260px}
.sun-box{position:absolute;left:225px;top:250px;width:172px;height:175px;background:radial-gradient(circle at 40% 20%,#fffbe0 0%,#fde37a 35%,#f7a84c 100%);text-align:center;font-size:8.5px;font-weight:700;color:var(--navy);padding-top:42px}
.sun-box .site{font-size:10.5px}
.social-row{display:flex;align-items:center;justify-content:center;gap:5px;margin:4px 0}
.social-square{width:15px;height:15px;background:var(--deep-blue)}
.divider{position:absolute;left:398px;top:0;width:1px;height:425px;background:rgba(255,255,255,.6)}
.hearts{position:absolute;left:410px;top:10px;width:210px;text-align:center;font-size:15px;font-weight:600;color:var(--violet)}
.pull-quote{position:absolute;left:412px;top:36px;width:206px;text-align:center;font-size:11px;font-weight:700;color:var(--violet);line-height:1.2}
.pull-quote .accent{color:var(--teal)}
.inside .photo{position:absolute;left:440px;top:88px;width:160px;height:160px}
.name{position:absolute;left:410px;top:262px;width:210px;text-align:center;font-size:15px;font-weight:600;color:var(--violet)}
.summary{position:absolute;left:410px;top:300px;width:206px;font-size:11px;font-weight:700;color:var(--deep-blue);line-height:1.2}
</style>
</head>
<body>

<section class="panel outside">
  <div class="bio">
    <p>Lorena Watkiss is an inspirational author and speaker. Her work has been featured on Gently Radiant, Morning Vessels, and Hymn &amp; Tea Journal (Fall 2011).</p>
    <p>Lorena is a wife and mother. She enjoys writing, spending time with her family, taking long walks, listening to music of all kinds, and experiencing God's daily gift-called life.</p>
    <p class="booking">To request Lorena Watkiss as a speaker for your church, meeting, or event please fill out the Booking Form available at:</p>
  </div>
  <div class="site-link">www.lorenawatkiss.example</div>

  <div class="first-book"><strong>Lorena's first book</strong>, Leaving the Lantern Hall: Revealing Hidden Snares in Ordinary Routines, is an informative memoir and Bible study, recounting her journey from committed Christian to witch, medium, and ghost hunter for eight years until restored to faith in Jesus Christ.</div>

  <div class="topics-band"></div>
  <div class="vertical-word authorship">AUTHORSHIP</div>
  <div class="vertical-word topics-word">TOPICS</div>
  <div class="topics-heading">Speaking Topics Include:</div>
  <ul class="topics-list">
    <li>Christians and the Occult</li>
    <li>Homelessness <small>(with Anson Watkiss)</small></li>
    <li>Human Trafficking</li>
    <li>Marriage Restoration <small>(with Anson Watkiss)</small></li>
    <li>Prayer as a Lifestyle</li>
    <li>Spiritual Warfare</li>
  </ul>

  <div class="photo" role="img" aria-label="Photo of Lorena Watkiss speaking into a microphone" style="background:linear-gradient(160deg,#d9c9b8,#8a6a58)"></div>
  <div class="credits">She was a <strong>contributing author</strong> to Walking the Shadow Road: A Plain Account of Dark Arts from Past Seekers by Dale Winterbottom and a <strong>consultant</strong> for the novel The Keeper of Pellam Hollow by Lumen Prize Winning Author, Norma Quillfeather.</div>

  <div class="books-band"></div>
  <div class="ribbon">A Double Dose of Information to Help Protect You and Your Family from the Onslaught of the Enemy</div>
  <div class="cover cover-one" role="img" aria-label="Book cover: Leaving the Lantern Hall" style="background:linear-gradient(#e9ecef,#8b98a5)"></div>
  <div class="cover cover-two" role="img" aria-label="Book cover: A Veteran's Map for Unseen Conflict" style="background:linear-gradient(#2e6b5f,#c8a94a)"></div>
  <div class="books-copy">
    <p>Former Witch and Medium Reveals Satan's Strategies from behind Enemy Lines Although we live in the physical world, our daily lives are connected–whether or not we realize it–to the spiritual battle raging around us. Having spent years as a medium, witch, and ghost hunter before being restored to her faith, Lorena Watkiss has been on the other side.</p>
    <p>Lorena's second book, A Veteran's Map for Unseen Conflict: 20 Field-Proven Tactics from Across Hostile Borders, will be published by Ridgeway Press for Fall 2014.</p>
  </div>
  <div class="store">Lorena's Books are available at:<br>Bookmarket.example/authorLorenaWatkiss</div>
</section>

<section class="panel inside">
  <div class="speaker-heading">What's Lorena Like as a Speaker?</div>
  <div class="quotes">
    <div class="quote">"The Women's Ministry at Lakeview Church in Marrowfield, MI invited Lorena Watkiss to speak at our Mother or Daughter Banquet earlier this month. I am so glad she accepted! We couldn't have chosen a speaker to fit in better than Lorena. She took our theme, "Instruments", and incorporated that into her speaking time with us. She used life examples and spoke directly into the hearts of the women and girls that attended our banquet. She even took time to speak to my teen aged daughters after the banquet as to why they should stay away from the paranormal. I highly recommend Lorena as a speaker and we hope to have her back at Lakeview Church in the near future!"<cite>~ Helen Drummond, Lakeview Community Church Women's Ministry</cite></div>
    <div class="quote">"Lorena came to our Hymn and Tea Night and shared her story; it was amazing! I've never seen women so riveted by a speaker! If you are in a position to bring Lorena to your church/event...do it!"<cite>~Ruth Pembly, Hymn and Tea Women's Ministry Events</cite></div>
    <div class="wrap-gap"></div><div class="wrap-box"></div>
    <div class="quote">"I was honored and delighted to have Lorena Watkiss be one of our speakers in the "Harvest Crossroads Seminar Tent" at Harvest Light Music Festival in Alder Bay, Michigan (one of the nation's top 10 Christian music festivals). Lorena has a unique testimony and style of speaking that keeps people, young and old, engaged into the heart of her message. Her stories of involvement in the occult and her conclusion of how God rescued her from these traps, answers many of the questions that people often have, but are afraid to ask when dealing with the "supernatural". If you are looking for a great speaker with a testimony that is relevant in today's culture of "curiosity in the supernatural", I highly recommend Lorena Watkiss to be on the top of your list of considerations."<cite>~ Glen Ashworth, Harvest Crossroads Seminar Tent, Coordinator</cite></div>
    <div class="quote">"Lorena's unique background and remarkable experiences, passion for the gospel message, and communication skills provide a wealth of information which will fit into any ministry setting. She has a heart for people and seeing the captives set free–and a delightful way of communicating God's message with joy!"<cite>~Carla Benning, Founder/Director, StepForward Fitness Ministry</cite></div>
  </div>

  <div class="sun-box">
    You can read more about Lorena at<br>
    <span class="site">www.lorenawatkiss.example</span>
    <div class="social-row"><span class="social-square"></span>or Visit her Social page</div>
    www.social.example/AuthorLorenaWatkiss
  </div>

  <div class="divider"></div>
  <div class="hearts">Inspiring Women's Hearts</div>
  <div class="pull-quote">"Lorena was an <span class="accent">ENTHUSIASTIC</span> and <span class="accent">WONDERFUL</span> from-the-heart speaker. We hope to have her back again!"</div>
  <div class="photo" role="img" aria-label="Headshot of Lorena Watkiss" style="background:linear-gradient(160deg,#e8d3c2,#6b4b3e)"></div>
  <div class="name">Lorena Watkiss</div>
  <div class="summary">When an ex witch and occultist devotes her energies to living and encouraging others for Christ, the result is a riveting encounter of faith, truth and devotion as a remedy for the traps and attacks of the enemy.</div>
</section>

</body>
</html>
```